Loyalty card for customers

I would like logo an a section for 10 places, so I can advertise 10th float is free, our business is health and wellness we offer magnesium float, hyperbaric oxygen and infrared sauna

```html
<!DOCTYPE html>
<html lang="en">
<head>
<meta charset="utf-8">
<title>Tidal Drift Loyalty Card</title>
<link href="https://fonts.googleapis.com/css2?family=Montserrat:wght@400;500;600;700&family=Oswald:wght@400;500&display=swap" rel="stylesheet">
<style>
  :root {
    --sheet-bg: #e6e6e6;
    --label-red: #f0141e;
    --navy-deep: #07263b;
    --navy-mid: #0f4565;
    --ocean-bright: #1a8fd0;
    --ocean-mid: #0d6aa3;
    --ice-blue: #8ccbeb;
    --band-blue: #86c9e8;
    --band-ink: #0b1f2c;
    --white: #ffffff;
    --black: #000000;
  }
  * { box-sizing: border-box; margin: 0; padding: 0; }
  html, body { width: 1200px; height: 800px; overflow: hidden; }
  body {
    background: radial-gradient(ellipse at 60% 20%, #f1f1f1 0%, var(--sheet-bg) 70%);
    font-family: "Montserrat", sans-serif;
    position: relative;
  }
  .option-label {
    position: absolute;
    color: var(--label-red);
    font-family: "Montserrat", sans-serif;
    font-size: 20px;
    font-weight: 500;
    letter-spacing: 1px;
    transform: translateX(-50%);
    white-space: nowrap;
  }
  .card {
    position: absolute;
    border-radius: 7px;
    overflow: hidden;
    box-shadow: 0 3px 10px rgba(0,0,0,0.18);
  }
  .card-front { width: 510px; height: 291px; }
  .card-front.narrow { width: 502px; height: 286px; }
  .front-1 { background: linear-gradient(160deg, var(--navy-mid) 0%, var(--navy-deep) 60%); }
  .front-2 { background: linear-gradient(160deg, var(--navy-mid) 0%, var(--navy-deep) 70%); }
  .front-3 { background: linear-gradient(170deg, var(--ocean-bright) 0%, var(--ocean-mid) 55%, var(--navy-mid) 100%); }
  .photo {
    position: absolute;
    top: 0;
  }
  .photo-floater {
    right: 0; width: 270px; height: 253px;
    background: radial-gradient(ellipse at 65% 45%, #1f5f86 0%, #123f5c 45%, rgba(7,38,59,0) 80%);
  }
  .photo-pod {
    right: 0; width: 240px; height: 250px;
    background: radial-gradient(ellipse at 60% 45%, #bfe8ff 0%, #4fb3e8 28%, #1a6c9c 55%, rgba(7,38,59,0) 82%);
  }
  .photo-relax {
    left: 0; width: 100%; height: 253px;
    background: linear-gradient(180deg, rgba(26,143,208,0) 0%, rgba(8,50,82,0.55) 60%, rgba(6,35,60,0.8) 100%);
  }
  .brand-name {
    position: absolute;
    left: 39px; top: 26px;
    color: var(--ice-blue);
    font-family: "Montserrat", sans-serif;
    font-weight: 600;
    font-size: 34px;
    line-height: 36px;
    letter-spacing: 7px;
    text-transform: lowercase;
  }
  .card-title {
    position: absolute;
    left: 73px; top: 104px;
    color: var(--white);
    font-family: "Oswald", sans-serif;
    font-size: 16px;
    letter-spacing: 2px;
  }
  .service-list {
    position: absolute;
    left: 51px; top: 168px;
    list-style: none;
    color: var(--white);
    font-size: 14.5px;
    line-height: 22.5px;
    letter-spacing: 0.4px;
  }
  .front-2 .service-list, .front-3 .service-list { color: var(--ice-blue); }
  .service-list li::before {
    content: "";
    display: inline-block;
    width: 4px; height: 4px;
    border-radius: 50%;
    background: #8aa6b8;
    margin-right: 7px;
    vertical-align: middle;
  }
  .contact-band {
    position: absolute;
    left: 0; bottom: 0;
    width: 100%; height: 38px;
    background: var(--band-blue);
    color: var(--band-ink);
    font-size: 14px;
    font-weight: 500;
    letter-spacing: 1px;
  }
  .website { position: absolute; left: 46px; top: 11px; }
  .social {
    position: absolute; left: 318px; top: 9px;
    display: flex; align-items: center; gap: 8px;
  }
  .social-dot { width: 18px; height: 18px; border-radius: 50%; background: var(--band-ink); }
  .social-handle { letter-spacing: 1px; }
  .card-back {
    width: 502px; height: 286px;
    background: var(--white);
  }
  .stamp-grid { position: absolute; left: 0; top: 0; }
  .free-text {
    font-family: "Montserrat", sans-serif;
    font-weight: 700;
    font-size: 16px;
    letter-spacing: 1px;
    fill: var(--white);
  }
  .offer-band {
    position: absolute;
    left: 0; top: 228px;
    width: 100%; height: 58px;
    background: var(--black);
    color: var(--white);
    font-size: 14.5px;
    letter-spacing: 2px;
    display: flex; align-items: center; justify-content: center;
  }
  .offer-band strong { font-weight: 700; margin-left: 5px; }
  .offer-band sup { font-size: 8px; }
</style>
</head>
<body>

  <div class="option-label" style="left:325px; top:64px;">FRONT - OPTION 1</div>
  <div class="option-label" style="left:895px; top:64px;">FRONT - OPTION 2</div>
  <div class="option-label" style="left:328px; top:740px;">FRONT - OPTION 3</div>
  <div class="option-label" style="left:894px; top:740px;">BACK DESIGN</div>

  <section class="card card-front front-1" style="left:89px; top:108px;">
    <div class="photo photo-floater" role="img" aria-label="Photo of a person floating in dark blue water"></div>
    <div class="brand-name">tidal<br>drift</div>
    <div class="card-title">LOYALTY CARD</div>
    <ul class="service-list">
      <li>MAGNESIUM FLOAT</li>
      <li>HYPERBARIC OXYGEN</li>
      <li>INFRARED SAUNA</li>
    </ul>
    <div class="contact-band">
      <span class="website">WWW.YOURSITE.COM</span>
      <span class="social"><span class="social-dot"></span><span class="social-handle">TidalDrift</span></span>
    </div>
  </section>

  <section class="card card-front narrow front-2" style="left:623px; top:113px;">
    <div class="photo photo-pod" role="img" aria-label="Photo of an open glowing float pod with a person floating inside"></div>
    <div class="brand-name">tidal<br>drift</div>
    <div class="card-title">LOYALTY CARD</div>
    <ul class="service-list">
      <li>MAGNESIUM FLOAT</li>
      <li>HYPERBARIC OXYGEN</li>
      <li>INFRARED SAUNA</li>
    </ul>
    <div class="contact-band">
      <span class="website">WWW.YOURSITE.COM</span>
      <span class="social" style="left:313px;"><span class="social-dot"></span><span class="social-handle">TidalDrift</span></span>
    </div>
  </section>

  <section class="card card-front front-3" style="left:89px; top:431px;">
    <div class="photo photo-relax" role="img" aria-label="Photo of a person resting in a blue-lit float pool"></div>
    <div class="brand-name" style="color:var(--white);">tidal<br>drift</div>
    <div class="card-title">LOYALTY CARD</div>
    <ul class="service-list">
      <li>MAGNESIUM FLOAT</li>
      <li>HYPERBARIC OXYGEN</li>
      <li>INFRARED SAUNA</li>
    </ul>
    <div class="contact-band">
      <span class="website">WWW.YOURSITE.COM</span>
      <span class="social"><span class="social-dot"></span><span class="social-handle">TidalDrift</span></span>
    </div>
  </section>

  <section class="card card-back" style="left:623px; top:431px;">
    <svg class="stamp-grid" width="502" height="228" viewBox="0 0 502 228">
      <g fill="none" stroke="#000" stroke-width="1" stroke-dasharray="4 3">
        <circle cx="81" cy="75" r="32"/>
        <circle cx="165" cy="75" r="32"/>
        <circle cx="248" cy="75" r="32"/>
        <circle cx="331" cy="75" r="32"/>
        <circle cx="415" cy="75" r="32"/>
        <circle cx="81" cy="155" r="32"/>
        <circle cx="165" cy="155" r="32"/>
        <circle cx="248" cy="155" r="32"/>
        <circle cx="331" cy="155" r="32"/>
      </g>
      <circle cx="415" cy="155" r="32" fill="#000"/>
      <text class="free-text" x="415" y="161" text-anchor="middle">FREE</text>
    </svg>
    <div class="offer-band">ENJOY 9 FLOATS &amp;<strong>GET 10<sup>TH</sup>&nbsp;&nbsp;&nbsp;FOR FREE</strong></div>
  </section>

</body>
</html>
```